TorvaLink.com

We need a new web design for our seo services website at torvalink.com.

Right now we have our homepage, and 2 other pages which we use a html code generator. We need a header and footer and a nice professional looking design to showcase our seo plans.

As for the logo we'll use our company torvagrid.com logo Torva and change Grid to Link and Search Engine Marketing to Search Engine Marketing.

We also like to display our brivopages widget and author alert sign up box.

```html
<!DOCTYPE html>
<html lang="en">
<head>
<meta charset="utf-8">
<title>TorvaLink – Internet Marketing and SEO Services</title>
<link href="https://fonts.googleapis.com/css2?family=Oxygen:wght@300;400;700&display=swap" rel="stylesheet">
<style>
:root{
  --red:#e0262b;
  --red-dark:#b3151a;
  --navy:#0c2466;
  --logo-blue:#1b3a8c;
  --ink:#555a60;
  --ink-soft:#6d7278;
  --page-bg:#e6e6e6;
  --panel:#f3f3f3;
  --rule:#c9c9c9;
  --white:#ffffff;
  --audit:#9a9b9d;
}
*{box-sizing:border-box;margin:0;padding:0}
html,body{width:1200px;height:900px;overflow:hidden}
body{font-family:"Oxygen",Arial,sans-serif;color:var(--ink);background:var(--page-bg);position:relative}
.abs{position:absolute}
.site-header{left:0;top:0;width:1200px;height:107px;background:var(--white)}
.brand{left:250px;top:40px;width:192px;font-size:36px;font-weight:700;color:var(--logo-blue);letter-spacing:-.8px;line-height:38px;white-space:nowrap}
.brand-sub{left:250px;top:80px;width:192px;text-align:right;font-size:12px;font-weight:700;color:var(--logo-blue);white-space:nowrap}
.search{left:689px;top:27px;width:155px;height:20px;display:flex}
.search-field{flex:1;border:1px solid #b9b9b9;border-radius:3px 0 0 3px;background:#fff;font-size:8px;color:#bbb;padding:5px 0 0 20px;position:relative}
.search-field svg{position:absolute;left:5px;top:4px}
.search-btn{width:39px;background:var(--red);color:#fff;font-size:8px;font-weight:700;text-align:center;line-height:20px;border-radius:0 3px 3px 0}
.btn{background:linear-gradient(#ef3a3f,var(--red-dark));color:#fff;font-weight:700;border-radius:3px;text-align:center;position:absolute;white-space:nowrap}
.btn::after{content:"";position:absolute;right:5px;top:50%;width:7px;height:7px;margin-top:-3.5px;border-radius:50%;background:#fff}
.login{left:856px;top:27px;width:94px;height:19px;font-size:9px;line-height:19px}
.tagline{right:250px;top:71px;font-size:13px;color:#585b5f;white-space:nowrap}
.hero{left:0;top:107px;width:1200px;height:216px;background:linear-gradient(90deg,#3a0306 0%,#a50d14 12%,#5c0408 22%,#c2111a 35%,#6a0509 50%,#c5121b 65%,#60040a 78%,#b10e16 90%,#3a0306 100%)}
.nav{left:249px;top:118px;display:flex;gap:3px}
.nav a{display:block;height:26px;line-height:26px;text-align:center;font-size:9px;color:#fff;text-decoration:none;background:rgba(245,170,175,.55);text-transform:uppercase}
.nav a.current{background:rgba(220,220,220,.85);color:#555}
.hero-title{left:296px;top:166px;font-size:23px;font-weight:300;color:#fff;line-height:34px;white-space:nowrap}
.hero-title b{font-weight:700}
.hero-copy{left:296px;top:240px;font-size:11.5px;color:#fff;line-height:16px}
.dots{left:296px;top:290px;display:flex;gap:4px}
.dots span{width:10px;height:10px;border-radius:50%;background:#d6d6d6}
.arrow{top:207px}
.hero-devices{left:562px;top:160px;width:306px;height:148px;background:linear-gradient(135deg,#d8dde4,#8d96a3 60%,#2b2e33);border-radius:6px}
.content{left:249px;top:337px;width:702px;height:435px;background:var(--panel)}
.section-title{font-size:24px;font-weight:300;color:var(--ink);white-space:nowrap}
.section-title span,.articles-title span{color:var(--red)}
.rule{height:1px;background:var(--rule)}
.plan{width:169px;height:116px;border-radius:3px;text-align:center;box-shadow:0 1px 3px rgba(0,0,0,.25)}
.plan.silver{background:linear-gradient(135deg,#b9bcc0,#f8f8f8 45%,#c8cacd)}
.plan.gold{background:linear-gradient(135deg,#e3a900,#fff1a4 45%,#d99a00)}
.plan.platinum{background:linear-gradient(135deg,#a5a8ac,#e8e9ea 50%,#a9acb0)}
.plan-name{font-size:13px;line-height:16px;font-weight:700;color:#5e6166;margin-top:15px;text-transform:uppercase}
.plan-name em{font-style:normal;color:var(--red)}
.plan-price{font-size:33px;color:var(--red);line-height:36px;letter-spacing:-1px}
.plan-price small{font-size:15px;letter-spacing:0}
.plan-note{font-size:6.5px;line-height:8px;font-weight:700;color:#222}
.plan .btn{left:30px;bottom:18px;width:108px;height:16px;font-size:7px;line-height:16px;padding-right:8px}
.signup-copy{left:292px;top:685px;font-size:11.5px;line-height:15px;color:var(--ink-soft)}
.field{left:430px;width:207px;height:18px;border:1px solid #b5b5b5;background:#fff;font-size:9px;color:#aaa;padding:3px 0 0 6px}
.articles-title{left:705px;top:357px;font-size:16px;font-weight:300;white-space:nowrap}
.article-list{left:705px;top:400px;list-style:none;font-size:10.5px;line-height:16px;color:#5b5f66;white-space:nowrap}
.audit{left:705px;top:477px;width:221px;height:279px;background:var(--audit);border-radius:6px}
.audit-title{left:718px;top:486px;color:#fff;font-size:15px;line-height:21px;font-weight:300}
.audit-title b{font-weight:700}
.audit-person{left:690px;top:565px;width:125px;height:155px;background:linear-gradient(180deg,#d9b9a2 0%,#3b3e45 35%,#222429 100%);border-radius:60px 60px 4px 4px}
.tiers{left:826px;top:488px;list-style:none;color:#fff;font-size:9px;line-height:14px;white-space:nowrap}
.tiers strong{display:block;margin-top:6px}
.tiers li:first-child strong{margin-top:0}
.more{left:721px;top:721px;width:94px;height:19px;font-size:9px;line-height:19px;padding-right:8px}
.site-footer{left:0;top:785px;width:1200px;height:115px;background:var(--navy);color:#fff}
.foot-head{top:801px;font-size:11px;font-weight:700;color:#fff}
.foot-links{left:271px;top:820px;list-style:none;font-size:8.5px;line-height:13px;color:#fff}
.foot-contact{left:367px;top:823px;font-size:9px;line-height:17px;color:#fff;white-space:nowrap}
.foot-contact .big{font-size:11px}
.social{left:535px;top:822px;display:flex;gap:8px}
.social span{width:24px;height:24px;background:#3d6aa8;border-radius:2px}
.copyright{left:729px;top:872px;font-size:7px;color:#fff;white-space:nowrap}
</style>
</head>
<body>
<header class="site-header abs">
  <div class="brand abs">TorvaLink</div>
  <div class="brand-sub abs">Search Engine Marketing</div>
  <div class="search abs">
    <div class="search-field"><svg width="10" height="10" viewBox="0 0 10 10"><circle cx="4" cy="4" r="3" fill="none" stroke="#777" stroke-width="1.4"/><line x1="6.3" y1="6.3" x2="9" y2="9" stroke="#777" stroke-width="1.6"/></svg>Search...</div>
    <div class="search-btn">Search</div>
  </div>
  <div class="btn login">LOGIN</div>
  <div class="tagline abs">TorvaLink Internet Marketing and Search Engine Optimization Services</div>
</header>

<section class="hero abs"></section>
<nav class="nav abs">
  <a class="current" href="#" style="width:101px">Home</a>
  <a href="#" style="width:142px">Local Marketing</a>
  <a href="#" style="width:151px">Competitive SEO</a>
  <a href="#" style="width:181px">Request a free qoute</a>
  <a href="#" style="width:116px">Contact</a>
</nav>
<svg class="arrow abs" style="left:246px" width="22" height="34" viewBox="0 0 22 34"><path d="M18 2 L5 17 L18 32" fill="none" stroke="#fff" stroke-width="6"/></svg>
<svg class="arrow abs" style="left:932px" width="22" height="34" viewBox="0 0 22 34"><path d="M4 2 L17 17 L4 32" fill="none" stroke="#fff" stroke-width="6"/></svg>
<h1 class="hero-title abs">Live Rank Tracking,<br>Reports &amp; <b>Much More</b></h1>
<p class="hero-copy abs">Lorem ipsum dolor sit amet, labore et<br>dolore magna ipsum dolor aliqua.</p>
<div class="dots abs"><span></span><span></span><span></span><span></span><span></span></div>
<div class="hero-devices abs" role="img" aria-label="Laptop, tablet and phone showing rank tracking dashboards"></div>

<main class="content abs"></main>
<h2 class="section-title abs" style="left:289px;top:348px">Organic Seo <span>Plans</span></h2>
<div class="rule abs" style="left:289px;top:386px;width:357px"></div>

<div class="plan silver abs" style="left:292px;top:404px">
  <div class="plan-name">Silver</div><div class="plan-price">$500<small>/mo</small></div><div class="plan-note">Up to 10 Keywords</div>
  <div class="btn">REQUEST A FREE QUOTE</div>
</div>
<div class="plan gold abs" style="left:473px;top:404px">
  <div class="plan-name">Gold</div><div class="plan-price">$750<small>/mo</small></div><div class="plan-note">Up to 10 Keywords</div>
  <div class="btn">REQUEST A FREE QUOTE</div>
</div>
<div class="plan platinum abs" style="left:291px;top:535px">
  <div class="plan-name">Platinum</div><div class="plan-price">$1200<small>/mo</small></div><div class="plan-note">Up to 10 Keywords</div>
  <div class="btn">REQUEST A FREE QUOTE</div>
</div>
<div class="plan platinum abs" style="left:473px;top:535px">
  <div class="plan-name">Platinum <em>Plus</em></div><div class="plan-price">$1300<small>/mo</small></div><div class="plan-note">Up to 10 Keywords</div>
  <div class="btn">REQUEST A FREE QUOTE</div>
</div>

<div class="rule abs" style="left:291px;top:671px;width:355px"></div>
<p class="signup-copy abs">Sign up to receive email<br>alerts of Elena Varga's<br>latest articles from<br>BrivoPages.com!</p>
<div class="field abs" style="top:687px">Name</div>
<div class="field abs" style="top:711px">Phone</div>
<div class="field abs" style="top:735px">Email</div>

<h2 class="articles-title abs">Articles by <span>Elena Varga</span></h2>
<div class="rule abs" style="left:705px;top:387px;width:221px"></div>
<ul class="article-list abs">
  <li>Different Kinds of Internet Marketing</li>
  <li>Seven Ways to Promote Your New Website</li>
  <li>Different Kinds of Internet Marketing</li>
  <li>Seven Ways to Promote Your New Website</li>
</ul>

<div class="audit abs"></div>
<div class="audit-title abs">Website Audit<br><b>MONTH 1<br>SETUP</b></div>
<ul class="tiers abs">
  <li><strong>10 Pages Optimized</strong>• Website Audit<br>• Keyword Research</li>
  <li><strong>20 Pages Optimized</strong>• Website Audit<br>• Keyword Research<br>• Keyword Grouping</li>
  <li><strong>30 Pages Optimized</strong>• Website Audit<br>• Keyword Research<br>• Keyword Grouping<br>• Keyword Mapping</li>
  <li><strong>40 Pages Optimized</strong>• Website Audit<br>• Keyword Research<br>• Keyword Grouping<br>• Keyword Mapping</li>
</ul>
<div class="audit-person abs" role="img" aria-label="Businesswoman in a dark suit presenting the audit offer"></div>
<div class="btn more">MORE INFO...</div>

<footer class="site-footer abs"></footer>
<div class="foot-head abs" style="left:271px">PAGES</div>
<ul class="foot-links abs">
  <li>Home</li><li>Local Marketing</li><li>Competitive SEO</li><li>Resquest Quote</li><li>Contact</li>
</ul>
<div class="foot-head abs" style="left:367px">CONTACT</div>
<div class="foot-contact abs">For all enquiries, contact our team<br><span class="big">Office <b>(02) 5550 1420</b></span><br><span class="big">Email <b>hello@torvalink.com.au</b></span></div>
<div class="foot-head abs" style="left:535px">FOLLOW US</div>
<div class="social abs" role="img" aria-label="Social network links"><span></span><span></span><span></span><span></span></div>
<div class="copyright abs">© 2013 TorvaLink Internet Marketing Service. All rights reserved.</div>
</body>
</html>
```